Marlow Crest Group (Real Estate and Investment)

A high end, clean design.
We are a real estate company with sales, asset management and investment divisions. We want to use a black and white scheme which is really high end feel. The back of the card can just be the logo (black background with the white writing) as we will probably emboss this when we print)

Target Market(s)

High level investors, high end houses for sale

Industry/Entity Type

Business

Contact Information for Business Card

Name, position, phone number and email address
Glen Varley, Managing Director, 0437259064 and glen@marlowcrest-example.com.au

Requirements
Must have
• Back of the card to be the black background with the white writing (as per the attached images). Would like the capacity to emboss the writing and logo

```html
<!DOCTYPE html>
<html lang="en">
<head>
<meta charset="utf-8">
<title>Marlow Crest Group – Business Card</title>
<link href="https://fonts.googleapis.com/css2?family=Raleway:wght@400;500&display=swap" rel="stylesheet">
<style>
  :root {
    --stage: #324e61;
    --card-front: #ffffff;
    --card-back: #222222;
    --ink: #555555;
    --ink-soft: #777777;
    --icon: #9a9a9a;
    --decor: #dedede;
    --white: #ffffff;
  }
  html, body {
    margin: 0;
    padding: 0;
    width: 1200px;
    height: 1200px;
    overflow: hidden;
    background: var(--stage);
    font-family: "Raleway", sans-serif;
  }
  .stage {
    position: relative;
    width: 1200px;
    height: 1200px;
  }
  .card {
    position: absolute;
    left: 108px;
    width: 985px;
    height: 563px;
    overflow: hidden;
  }
  .card--front { top: 27px; background: var(--card-front); }
  .card--back  { top: 610px; background: var(--card-back); }

  .identity {
    position: absolute;
    left: 58px;
    top: 108px;
    display: inline-block;
    text-align: right;
  }
  .identity__name {
    margin: 0;
    font-size: 62px;
    font-weight: 500;
    line-height: 1;
    color: var(--ink);
    letter-spacing: -0.5px;
  }
  .identity__role {
    margin: 8px 0 0;
    font-size: 18px;
    font-weight: 400;
    color: var(--ink-soft);
    letter-spacing: 0.3px;
  }

  .contacts {
    position: absolute;
    left: 58px;
    top: 414px;
    margin: 0;
    padding: 0;
    list-style: none;
  }
  .contacts__item {
    display: flex;
    align-items: center;
    height: 30px;
    margin-bottom: 15px;
    font-size: 22px;
    color: var(--ink);
  }
  .contacts__item--phone { font-weight: 500; }
  .contacts__icon {
    width: 28px;
    height: 28px;
    margin-right: 21px;
    flex: none;
  }

  .front-decor {
    position: absolute;
    left: 474px;
    top: 45px;
  }

  .brand {
    position: absolute;
    left: 0;
    right: 0;
    top: 0;
    bottom: 0;
  }
  .brand__mark {
    position: absolute;
    left: 414px;
    top: 164px;
  }
  .brand__name {
    position: absolute;
    left: 0;
    right: 0;
    top: 355px;
    margin: 0;
    text-align: center;
    font-size: 38px;
    font-weight: 500;
    color: var(--white);
    letter-spacing: 1px;
  }
</style>
</head>
<body>
<main class="stage">

  <section class="card card--front" aria-label="Business card front">
    <div class="identity">
      <h1 class="identity__name">Glen Varley</h1>
      <p class="identity__role">MANAGING DIRECTOR</p>
    </div>

    <ul class="contacts">
      <li class="contacts__item contacts__item--phone">
        <svg class="contacts__icon" viewBox="0 0 28 28" aria-hidden="true">
          <rect x="7" y="1.5" width="14" height="25" rx="2" fill="none" stroke="var(--icon)" stroke-width="2"/>
          <line x1="7" y1="21" x2="21" y2="21" stroke="var(--icon)" stroke-width="1.5"/>
          <circle cx="14" cy="23.7" r="1" fill="var(--icon)"/>
        </svg>
        04 3725 9064
      </li>
      <li class="contacts__item">
        <svg class="contacts__icon" viewBox="0 0 28 28" aria-hidden="true">
          <rect x="1.5" y="5" width="25" height="18" fill="none" stroke="var(--icon)" stroke-width="2"/>
          <polyline points="1.5,5 14,15 26.5,5" fill="none" stroke="var(--icon)" stroke-width="1.5"/>
          <polyline points="1.5,23 11,13.5 M17,13.5 26.5,23" fill="none" stroke="var(--icon)" stroke-width="1.5"/>
        </svg>
        glen@marlowcrest-example.com.au
      </li>
    </ul>

    <svg class="front-decor" width="472" height="472" viewBox="0 0 472 472" aria-hidden="true">
      <circle cx="236" cy="236" r="233" fill="none" stroke="var(--decor)" stroke-width="4"/>
    </svg>
  </section>

  <section class="card card--back" aria-label="Business card back">
    <div class="brand">
      <svg class="brand__mark" width="156" height="156" viewBox="0 0 156 156" aria-hidden="true">
        <circle cx="78" cy="78" r="76" fill="none" stroke="var(--white)" stroke-width="2"/>
      </svg>
      <p class="brand__name">MARLOW CREST GROUP</p>
    </div>
  </section>

</main>
</body>
</html>
```